artist "stamp" design

Im a young artist. I`m making a stamp with my information so i can make homemade business cards, so I need the following information to look good together and simple to read:

Lucila Marbán Oteiza

www.lumaroti.com

lucilamo47@vextramail.com

i want a very clan look, but with some personality. a simple logo or "look" would be great but nothing to fancy.

An idea I had was to make it look like it was written with a typewriter or a concept like that...be creative! thank you!
Updates

I don't want any image or icon, just letters, I need it to be compacto, I'm making a stamp

I don't want it to say photography 

I dont want my name to take over so it should stay close to the size as the rest of the info.

all my info should be included, this is not a logo its a design for a stamp meant to fin in a business card.

Target Market(s)

I'm a photographer, I want something very simple and I need this to make a stamp that ill use to pit on my cards and CV. I want something simple and modern

Industry/Entity Type

Business

Logo Text

Lucila Marbán Oteiza

Logo styles of interest
Abstract Logo
Wordmark Logo
Lettermark Logo
Font styles to use
Serif
Sans Serif

Requirements
Must have
• Has to look young and fresh
Nice to have
• Have to see how it looks on a business card with website and and email
Should not have
• Images

```html
<!DOCTYPE html>
<html lang="en">
<head>
<meta charset="utf-8">
<title>Lucila Marbán Oteiza — Stamp</title>
<link rel="stylesheet" href="https://fonts.googleapis.com/css2?family=Courier+Prime&display=swap">
<style>
  :root {
    --paper: #ffffff;
    --ink: #111111;
  }
  html, body {
    margin: 0;
    padding: 0;
    width: 1200px;
    height: 1000px;
    overflow: hidden;
    background: var(--paper);
  }
  .stamp-canvas {
    width: 1200px;
    height: 1000px;
    display: flex;
    align-items: center;
    justify-content: center;
  }
  .stamp {
    width: 900px;
    height: auto;
  }
  .stamp .band,
  .stamp .edge {
    fill: none;
    stroke: var(--ink);
    stroke-width: 0.7;
    stroke-linejoin: miter;
  }
  .stamp .band-face {
    fill: var(--paper);
  }
  .stamp .info {
    font-family: "Courier Prime", "Courier New", monospace;
    font-size: 11px;
    fill: var(--ink);
    text-anchor: middle;
    dominant-baseline: central;
    letter-spacing: 0.4px;
  }
  .stamp .facet-letter {
    font-family: "Courier Prime", "Courier New", monospace;
    font-size: 10px;
    fill: var(--ink);
    text-anchor: middle;
    dominant-baseline: central;
  }
</style>
</head>
<body>
<main class="stamp-canvas">
  <svg class="stamp" viewBox="-4 -4 306 116" xmlns="http://www.w3.org/2000/svg" aria-label="Contact stamp for Lucila Marbán Oteiza">
    <!-- name band -->
    <polygon class="band band-face" points="0,0 280,0 298,36 18,36"/>
    <text class="info info-name" x="149" y="18">Lucila Marbán Oteiza</text>

    <!-- website band -->
    <polygon class="band band-face" points="38,36 280,36 262,72 20,72"/>
    <polygon class="band" points="18,36 38,36 20,72 0,72"/>
    <line class="edge" x1="286" y1="36" x2="268" y2="72"/>
    <line class="edge" x1="292" y1="36" x2="274" y2="72"/>
    <line class="edge" x1="298" y1="36" x2="280" y2="72"/>
    <text class="facet-letter" x="19" y="54" transform="skewX(-10) translate(9.5 0)">W</text>
    <text class="info info-web" x="150" y="54">www.lumaroti.com</text>

    <!-- email band -->
    <polygon class="band band-face" points="20,72 262,72 280,108 38,108"/>
    <line class="edge" x1="0" y1="72" x2="18" y2="108"/>
    <line class="edge" x1="6" y1="72" x2="24" y2="108"/>
    <line class="edge" x1="12" y1="72" x2="30" y2="108"/>
    <line class="edge" x1="18" y1="108" x2="38" y2="108"/>
    <polygon class="band" points="262,72 280,72 298,108 280,108"/>
    <text class="facet-letter" x="280" y="90" transform="rotate(-90 280 90)">E</text>
    <text class="info info-email" x="150" y="90">lucilamo47@vextramail.com</text>
  </svg>
</main>
</body>
</html>
```